KerrLow Farm

Need a nice simple clean double sided business card that has our logo and info on:
Kerr Low Farm
Martin & Felicity Kerr Low
kerrlowfarm@mailbarn.example
Martin: 1-780-555-0148
Felicity: 1-780-555-0193
Instagram @ kerrlow_farm

Contact Information for Business Card

Martin & Felicity Kerr Low kerrlowfarm@mailbarn.example Martin: 1-780-555-0148 Felicity: 1-780-555-0193

```html
<!DOCTYPE html>
<html lang="en">
<head>
<meta charset="utf-8">
<title>Kerr Low Farm – Business Card</title>
<link rel="stylesheet" href="https://fonts.googleapis.com/css2?family=Cinzel:wght@500&family=Montserrat:wght@400;700&display=swap">
<style>
  :root {
    --backdrop: #d3d6d6;
    --card: #f3f3f1;
    --green: #5ea51f;
    --orange: #f5a623;
    --ink: #6b6b6b;
  }
  * { box-sizing: border-box; margin: 0; padding: 0; }
  html, body { width: 1200px; height: 1051px; overflow: hidden; }
  body {
    background: var(--backdrop);
    display: flex;
    flex-direction: column;
    align-items: center;
    justify-content: center;
    gap: 60px;
    font-family: "Montserrat", sans-serif;
  }
  .card {
    width: 620px;
    height: 354px;
    background: var(--card);
    border-bottom: 6px solid var(--green);
    box-shadow: 0 10px 28px rgba(0,0,0,0.18);
    display: flex;
    align-items: center;
    justify-content: center;
  }
  .brand {
    display: flex;
    align-items: center;
    gap: 14px;
  }
  .brand-dot {
    width: 20px;
    height: 20px;
    border: 3px solid var(--green);
    border-radius: 50%;
  }
  .brand-name {
    font-family: "Cinzel", serif;
    font-weight: 500;
    color: var(--green);
    font-size: 34px;
    letter-spacing: 0.5px;
    white-space: nowrap;
  }
  .card--back { justify-content: flex-start; padding: 0 30px; }
  .card--back .brand-name { font-size: 24px; }
  .card--back .brand-dot { width: 16px; height: 16px; }
  .brand-panel {
    width: 270px;
    display: flex;
    justify-content: center;
  }
  .divider {
    width: 2px;
    height: 190px;
    background: var(--green);
    margin: 0 26px 0 10px;
  }
  .contact-name {
    color: var(--green);
    font-weight: 700;
    font-size: 19px;
    line-height: 1.25;
    margin-bottom: 12px;
  }
  .contact-list { list-style: none; }
  .contact-list li {
    display: flex;
    align-items: center;
    gap: 8px;
    color: var(--ink);
    font-size: 13px;
    line-height: 1.75;
    white-space: nowrap;
  }
  .contact-list svg { width: 12px; height: 12px; flex: none; }
  .social-mark {
    width: 11px; height: 11px;
    border: 1.5px solid var(--orange);
    border-radius: 2px;
    flex: none;
  }
</style>
</head>
<body>
  <section class="card card--front">
    <div class="brand">
      <span class="brand-dot"></span>
      <span class="brand-name">Kerr Low Farm</span>
    </div>
  </section>

  <section class="card card--back">
    <div class="brand-panel">
      <div class="brand">
        <span class="brand-dot"></span>
        <span class="brand-name">Kerr Low Farm</span>
      </div>
    </div>
    <div class="divider"></div>
    <div class="contact">
      <p class="contact-name">Martin &amp;<br>Felicity Kerr Low</p>
      <ul class="contact-list">
        <li>
          <svg viewBox="0 0 24 24"><path fill="var(--orange)" d="M6.6 10.8a15.1 15.1 0 0 0 6.6 6.6l2.2-2.2a1 1 0 0 1 1-.25 11.4 11.4 0 0 0 3.6.57 1 1 0 0 1 1 1V20a1 1 0 0 1-1 1A17 17 0 0 1 3 4a1 1 0 0 1 1-1h3.5a1 1 0 0 1 1 1c0 1.25.2 2.45.57 3.57a1 1 0 0 1-.25 1z"/></svg>
          1-780-555-0148 Martin
        </li>
        <li>
          <svg viewBox="0 0 24 24"><path fill="var(--orange)" d="M6.6 10.8a15.1 15.1 0 0 0 6.6 6.6l2.2-2.2a1 1 0 0 1 1-.25 11.4 11.4 0 0 0 3.6.57 1 1 0 0 1 1 1V20a1 1 0 0 1-1 1A17 17 0 0 1 3 4a1 1 0 0 1 1-1h3.5a1 1 0 0 1 1 1c0 1.25.2 2.45.57 3.57a1 1 0 0 1-.25 1z"/></svg>
          1-780-555-0193 Felicity
        </li>
        <li>
          <svg viewBox="0 0 24 24"><path fill="var(--orange)" d="M2 5h20v14H2z"/><path fill="none" stroke="var(--card)" stroke-width="2" d="M2 6l10 7 10-7"/></svg>
          kerrlowfarm@mailbarn.example
        </li>
        <li>
          <span class="social-mark"></span>
          @ kerrlow_farm
        </li>
      </ul>
    </div>
  </section>
</body>
</html>
```